Milk/ Greek yoghurt Packaging design

We need a packaging design for a new dairy processing company based in Kabul called Varnel Dairy. We produce high quality dairy products such as milk, yoghurt, yoghurt drinks. We produce high end Greek yoghurt, milk, salted yoghurt drink called Doogh or Ayran.
The design will be used for three products types.
- Greek yoghurt:50 ml, 250 ml, 400 ml cup packaging
- Ayran(Doogh) 250 ml, 350 ml cup packaing
- Pasteurized milk s 500 ml 1000 ml bottles
Packaging should have the following attritubes
- High end and premium look
- Modern look with lines and fonts
- Information should be both in English and Dari ( we can provide the dari text)
- slogan Premium yoghurt should be mentioned under de logo
We are very inspired by Lustreka yoghurt. Please see the Lustreka packaging for inspiration.
Text for backside of the cup will be provided in two days.
We have two designs for logo. Please see the logo where the cow is on the letter of 'Varnel'. I do not have this logo sperately in good quality.
Regards
محصول از شرکت تولد لبنات ورنل تهیه شده ا با استارتر در چربی ٪3/+ ٪2/
Please mention the sizes of packaging with an error range
± of 10 gram.
Target Market(s)
Kabul,
High end, premium
Industry/Entity Type
It Company
Requirements
Must have
- Modern design, elegant, catchy
Nice to have
- grass

```html
<!DOCTYPE html>
<html lang="en">
<head>
<meta charset="utf-8">
<title>Varnel Dairy – Greek Yoghurt Packaging</title>
<link href="https://fonts.googleapis.com/css2?family=Cinzel:wght@400;600;700&family=Montserrat:wght@400;500;600;700&display=swap" rel="stylesheet">
<style>
  :root{
    --navy:#1d4f8a;
    --navy-dark:#163d6b;
    --gold:#c99630;
    --gold-light:#f2d47c;
    --gold-deep:#9c6b16;
    --cream:#fbf6e8;
    --ink:#222;
    --paper:#ffffff;
    --backdrop:#ebebeb;
    --cream-shadow:#dcdcdc;
  }
  *{box-sizing:border-box;margin:0;padding:0}
  html,body{width:1200px;height:1000px;overflow:hidden}
  body{background:var(--backdrop);font-family:"Montserrat",Arial,sans-serif;color:var(--ink);position:relative}

  /* Header block */
  .brand-header{position:absolute;right:70px;top:130px;width:280px;text-align:center}
  .brand-header .brand-name{font-family:"Montserrat",sans-serif;font-weight:700;font-size:84px;color:var(--navy);line-height:1;letter-spacing:-1px}
  .brand-header .title{margin-top:22px;font-weight:600;font-size:22px;letter-spacing:1px;color:#111}
  .brand-header .sizes{margin-top:4px;font-size:15px;color:#333;letter-spacing:.5px}

  /* Label panels */
  .label{position:absolute;top:370px;width:330px;height:420px;background:var(--paper);box-shadow:0 6px 18px rgba(0,0,0,.12);overflow:hidden}
  .label-back{left:40px}
  .label-front{left:390px}
  .gold-band{position:absolute;left:0;right:0;height:40px;background:linear-gradient(90deg,var(--gold-deep),var(--gold-light) 30%,var(--gold) 55%,var(--gold-light) 80%,var(--gold-deep))}
  .gold-band.top{top:0}
  .gold-band.bottom{bottom:0;height:24px}
  .band-text{position:absolute;top:12px;width:100%;text-align:center;font-weight:700;font-size:11.5px;color:#fff;letter-spacing:.4px}

  .front-brand{position:absolute;top:100px;width:100%;text-align:center;font-weight:700;font-size:58px;color:var(--navy);line-height:1}
  .ribbon{position:absolute;left:50%;transform:translateX(-50%);width:190px;height:24px;background:linear-gradient(180deg,var(--gold-light),var(--gold) 60%,var(--gold-deep));color:var(--cream);font-family:"Cinzel",serif;font-size:12px;letter-spacing:1px;text-align:center;line-height:24px;clip-path:polygon(0 0,100% 0,95% 50%,100% 100%,0 100%,5% 50%)}
  .label-front .ribbon{top:172px}
  .product{position:absolute;width:100%;text-align:center;font-family:"Cinzel",serif;font-weight:600;font-size:19px;color:#333;letter-spacing:.5px}
  .label-front .product{top:206px}
  .photo-swirl{position:absolute;background:radial-gradient(ellipse at 55% 45%,#ffffff 0%,#f1f1f1 45%,var(--cream-shadow) 100%)}
  .label-front .photo-swirl{top:236px;left:20px;right:20px;height:90px;border-radius:50%}
  .weight{position:absolute;left:24px;font-weight:700;font-size:12px;color:#222}
  .weight small{font-weight:500;font-size:8px}
  .label-front .weight{top:334px}
  .variant{position:absolute;width:100%;text-align:center;font-family:"Cinzel",serif;font-weight:600;font-size:11px;color:#222;letter-spacing:.5px}
  .label-front .variant{top:352px}
  .gold-rule{position:absolute;left:40px;right:40px;height:1px;background:var(--gold)}
  .label-front .gold-rule{top:368px}
  .dari-line{position:absolute;top:374px;width:100%;text-align:center;font-size:9px;color:#333;direction:rtl}

  /* Back panel */
  .nutrition{position:absolute;top:58px;left:20px;width:150px;border-right:1px solid #222;padding-right:6px;font-size:6.5px}
  .nutrition h3{font-weight:700;font-size:11px;border-bottom:1px solid #222;padding-bottom:1px}
  .nutrition .serving{font-size:7px;font-weight:600;border-bottom:3px solid #222;padding:1px 0}
  .nutrition table{width:100%;border-collapse:collapse}
  .nutrition td{border-bottom:1px solid #999;padding:1px 0}
  .nutrition td.num{text-align:right}
  .nutrition tr.heavy td{border-bottom:3px solid #222}
  .nutrition .note{margin-top:4px;line-height:1.35}
  .back-copy{position:absolute;left:20px;width:150px;font-size:6.5px;line-height:1.4}
  .back-copy.one{top:258px}
  .back-copy.two{top:288px}
  .label-back .weight{top:334px}
  .label-back .variant{top:352px;left:100px}

  /* Lid */
  .lid{position:absolute;left:740px;top:400px;width:440px;height:420px}
</style>
</head>
<body>

<header class="brand-header">
  <div class="brand-name">Varnel</div>
  <div class="title">PACKAGING DESIGN</div>
  <div class="sizes">(SIZE : 50ML /250 ML/ 500ML)</div>
</header>

<section class="label label-back" aria-label="Back label">
  <div class="gold-band top" role="img" aria-label="Gold band with sparkling light pattern"></div>
  <div class="nutrition">
    <h3>NUTRITION FACTS</h3>
    <div class="serving">SERVING SIZE 100G</div>
    <table>
      <tr><td>AMOUNT PER SERVING</td><td class="num"></td></tr>
      <tr><td>CALORIES 63 &nbsp;CALORIES FROM FAT</td><td class="num">14</td></tr>
      <tr><td>TOTAL FAT &nbsp;1.55G</td><td class="num">3%</td></tr>
      <tr><td>CHOLESTEROL &nbsp;6 MG</td><td class="num">2%</td></tr>
      <tr><td>SODIUM &nbsp;70 MG</td><td class="num">3%</td></tr>
      <tr><td>POTASSIUM &nbsp;234 MG</td><td class="num"></td></tr>
      <tr><td>TOTAL CARBOHYDRATE &nbsp;7.04G</td><td class="num">2%</td></tr>
      <tr class="heavy"><td>PROTEIN &nbsp;5.25G</td><td class="num"></td></tr>
      <tr><td>VITAMIN A</td><td class="num">1%</td></tr>
      <tr><td>VITAMIN C</td><td class="num">1%</td></tr>
      <tr><td>CALCIUM</td><td class="num">18%</td></tr>
      <tr><td>IRON</td><td class="num">0%</td></tr>
    </table>
    <p class="note">Percent daily values are based on a 2000 calorie diet. Your daily values may be higher or lower depending on your calorie needs.</p>
  </div>
  <p class="back-copy one">Keep refrigerated between 2 and 6°C. Consume within three days of opening. Stir gently before serving.</p>
  <p class="back-copy two">Made from fresh local milk with live active cultures. No added sugar, thickeners or preservatives.</p>
  <div class="weight">500GR <small>(±10GR)</small></div>
  <div class="variant">PLAIN</div>
  <div class="gold-band bottom" role="img" aria-label="Gold band with sparkling light pattern"></div>
</section>

<section class="label label-front" aria-label="Front label">
  <div class="gold-band top" role="img" aria-label="Gold band with sparkling light pattern">
    <div class="band-text">ONLY NATURAL SOURCED INGREDIANTS</div>
  </div>
  <div class="front-brand">Varnel</div>
  <div class="ribbon">PREMIUM QUALITY</div>
  <div class="product">GREEK YOGHURT</div>
  <div class="photo-swirl" role="img" aria-label="Photo of a creamy yoghurt swirl with a spoonful of yoghurt"></div>
  <div class="weight">500GR <small>(±10GR)</small></div>
  <div class="variant">PLAIN</div>
  <div class="gold-rule"></div>
  <div class="dari-line">محصول از شرکت تولید لبنیات ورنل تهیه شده با استارتر در چربی ٪3</div>
  <div class="gold-band bottom" role="img" aria-label="Gold band with sparkling light pattern"></div>
</section>

<svg class="lid" viewBox="0 0 440 420" role="group" aria-label="Cup lid">
  <defs>
    <linearGradient id="goldRing" x1="0" y1="0" x2="1" y2="1">
      <stop offset="0" stop-color="#9c6b16"/>
      <stop offset=".3" stop-color="#f2d47c"/>
      <stop offset=".55" stop-color="#c99630"/>
      <stop offset=".8" stop-color="#f2d47c"/>
      <stop offset="1" stop-color="#9c6b16"/>
    </linearGradient>
    <linearGradient id="ribbonGold" x1="0" y1="0" x2="0" y2="1">
      <stop offset="0" stop-color="#f2d47c"/>
      <stop offset=".6" stop-color="#c99630"/>
      <stop offset="1" stop-color="#9c6b16"/>
    </linearGradient>
    <radialGradient id="swirl" cx=".55" cy=".45" r=".6">
      <stop offset="0" stop-color="#ffffff"/>
      <stop offset=".5" stop-color="#f1f1f1"/>
      <stop offset="1" stop-color="#dcdcdc"/>
    </radialGradient>
    <path id="arcTop" d="M 45 210 A 155 155 0 0 1 355 210"/>
    <path id="arcBottom" d="M 32 210 A 168 168 0 0 0 368 210"/>
  </defs>
  <polygon points="380,150 434,172 434,248 380,270" fill="url(#goldRing)" role="img" aria-label="Gold peel tab"/>
  <text x="416" y="210" transform="rotate(-90 416 210)" text-anchor="middle" dominant-baseline="middle" font-family="Montserrat, sans-serif" font-weight="700" font-size="9" fill="#fff">PEEL HERE</text>
  <circle cx="200" cy="210" r="195" fill="url(#goldRing)" role="img" aria-label="Gold ring with sparkling light pattern"/>
  <circle cx="200" cy="210" r="173" fill="#fff"/>
  <g font-family="Montserrat, sans-serif" font-size="10" fill="#1d4f8a" letter-spacing="2">
    <text><textPath href="#arcTop" startOffset="50%" text-anchor="middle">GREEK YOGHURT · ONLY NATURAL SOURCE INGREDIENTS</textPath></text>
    <text><textPath href="#arcBottom" startOffset="50%" text-anchor="middle">ONLY NATURAL SOURCE INGREDIENTS</textPath></text>
  </g>
  <text x="200" y="168" text-anchor="middle" font-family="Montserrat, sans-serif" font-weight="700" font-size="50" fill="#1d4f8a">Varnel</text>
  <polygon points="110,186 290,186 282,198 290,210 110,210 118,198" fill="url(#ribbonGold)"/>
  <text x="200" y="203" text-anchor="middle" font-family="Cinzel, serif" font-size="12" fill="#fbf6e8" letter-spacing="1">PREMIUM QUALITY</text>
  <text x="200" y="238" text-anchor="middle" font-family="Cinzel, serif" font-weight="600" font-size="18" fill="#333">GREEK YOGHURT</text>
  <ellipse cx="200" cy="286" rx="130" ry="40" fill="url(#swirl)" role="img" aria-label="Photo of a creamy yoghurt swirl with a spoonful of yoghurt"/>
  <text x="200" y="346" text-anchor="middle" font-family="Cinzel, serif" font-weight="600" font-size="13" fill="#1d4f8a">PLAIN</text>
</svg>

</body>
</html>
```